Website Design - Financial Services Software

We are looking for website designs for our public website.
Some competitor sites we like are
www.torvani.com.au
www.pluma.com.au
www.quentabridge.com
www.morlupa.com.au

A wireframe example of our site can be found at
http://pr4tqz.bivlowpage.com/

Attached is our logo.

Industry/Entity Type

Financial

```html
<!DOCTYPE html>
<html lang="en">
<head>
<meta charset="utf-8">
<title>Veridane — Smarter Financial Strategies</title>
<link href="https://fonts.googleapis.com/css2?family=Open+Sans:wght@400;600&family=Ubuntu:wght@400;500&display=swap" rel="stylesheet">
<style>
:root{
  --gold:#e3c25a;
  --gold-deep:#c9a03a;
  --gold-grad-top:#ebc76a;
  --gold-grad-bot:#c99b36;
  --brown:#8a5a1c;
  --ink:#2f3a3a;
  --text:#555a5a;
  --muted:#6b6f6f;
  --line:#c9c9c9;
  --white:#ffffff;
  --footer:#efefef;
  --icon:#4a4a4a;
}
*{box-sizing:border-box;margin:0;padding:0}
html,body{width:1145px;height:1200px;overflow:hidden;background:var(--white)}
body{font-family:"Open Sans",sans-serif;color:var(--text);position:relative}
a{color:inherit;text-decoration:none}

.top-rule{position:absolute;left:0;top:0;width:1145px;height:4px;background:var(--gold)}
.site-header{position:absolute;left:0;top:4px;width:1145px;height:132px;background:var(--white);border-bottom:1px solid #cfcfcf;box-shadow:0 1px 3px rgba(0,0,0,.15)}
.brand{position:absolute;left:146px;top:50px;display:flex;align-items:center;gap:10px}
.brand-mark{width:28px;height:28px;background:var(--gold-deep)}
.brand-name{font-family:"Open Sans",sans-serif;font-weight:600;font-size:22px;color:var(--brown);letter-spacing:1px}
.login{position:absolute;left:923px;top:14px;width:77px;height:27px;border:1px solid #c6a640;border-radius:3px;background:linear-gradient(#f0d98a,#dcbf5e);font-size:11px;color:#5a4a20;text-align:center;line-height:25px}
.main-nav{position:absolute;top:64px;left:632px;display:flex;gap:0}
.main-nav a{font-size:15px;color:#222;height:28px;line-height:26px;padding:0 8px}
.main-nav .is-current{border:1px solid var(--brown);border-radius:3px;color:var(--brown)}
.main-nav .nav-examples{margin-left:38px}
.main-nav .nav-faq{margin-left:46px}
.main-nav .nav-about{margin-left:46px}

.hero{position:absolute;left:0;top:137px;width:1145px;height:454px;background:linear-gradient(180deg,#d5d5d5 0%,#c4c4c4 45%,#9a9a9a 80%,#7d7d7d 100%);border-bottom:2px solid var(--gold)}
.hero-title{position:absolute;left:145px;top:118px;font-family:"Ubuntu",sans-serif;font-weight:500;font-size:27px;color:var(--ink)}
.hero-lead{position:absolute;left:146px;top:172px;width:360px;font-size:19px;line-height:36px;color:#3c4444}
.btn{position:absolute;height:37px;border-radius:3px;font-size:13px;text-align:center;line-height:35px}
.btn-gold{left:146px;top:286px;width:155px;background:linear-gradient(var(--gold-grad-top),var(--gold-grad-bot));border:1px solid #b88a2c;color:#3a2c10}
.btn-outline{left:310px;top:286px;width:155px;background:var(--white);border:1px solid #bbb;color:#222}
.video-frame{position:absolute;left:520px;top:92px;width:481px;height:276px;background:var(--white);border:1px solid #d0d0d0;padding:9px}
.video-still{width:100%;height:100%;background:linear-gradient(135deg,#e9e4dc 0%,#cdbfa8 45%,#8b8275 100%)}

.features-intro{position:absolute;left:146px;top:626px;width:200px}
.features-intro h2{font-family:"Ubuntu",sans-serif;font-weight:400;font-size:21px;line-height:28px;color:var(--ink)}
.features-intro p{font-size:11px;line-height:20px;color:var(--text);margin-top:14px}
.features-intro p + p{margin-top:20px}

.feature-card{position:absolute;width:200px;height:100px;border:1px solid var(--line);border-radius:4px;background:var(--white);padding:5px 8px}
.feature-card h3{font-family:"Ubuntu",sans-serif;font-weight:400;font-size:15px;color:var(--ink)}
.feature-card p{font-size:10px;line-height:16px;color:var(--muted);margin-top:4px;width:140px}
.feature-card .more{font-size:10px;color:var(--muted);margin-top:8px;display:flex;align-items:center;gap:6px}
.feature-card svg.icon{position:absolute;right:9px;top:28px;width:46px;height:46px}
.feature-card.is-featured{background:linear-gradient(var(--gold-grad-top),var(--gold-grad-bot));border-color:#c09a40}
.feature-card.is-featured p,.feature-card.is-featured .more{color:#6a4e18}

.divider{position:absolute;left:146px;top:939px;width:854px;border-top:1px dashed #b5b5b5}
.cta-text{position:absolute;left:250px;top:977px;font-size:19px;color:#3c4444}
.cta-btn{position:absolute;left:742px;top:973px;width:154px;height:36px;border:1px solid var(--brown);border-radius:3px;font-size:13px;color:#222;text-align:center;line-height:34px}

.site-footer{position:absolute;left:0;top:1045px;width:1145px;height:155px;background:var(--footer)}
.footer-rule{position:absolute;left:130px;top:0;width:880px;height:3px;background:linear-gradient(90deg,transparent,var(--brown) 10%,var(--gold-deep) 50%,var(--brown) 90%,transparent)}
.footer-brand{position:absolute;left:146px;top:62px;display:flex;align-items:center;gap:8px}
.footer-brand .brand-mark{width:20px;height:20px}
.footer-brand .brand-name{font-size:17px}
.footer-col{position:absolute;top:27px;width:127px}
.footer-col h4{font-family:"Ubuntu",sans-serif;font-weight:400;font-size:15px;color:#222;padding-bottom:5px;border-bottom:1px solid #555}
.footer-col ul{list-style:none;margin-top:10px}
.footer-col li{font-size:11px;color:#555;line-height:22px;display:flex;align-items:center;gap:8px}
.dot{width:16px;height:16px;border-radius:50%;display:inline-block}
.dot-grey{background:#a7a7a7}
.dot-blue{background:#7fd3ea}
.copyright{position:absolute;left:146px;top:138px;font-size:10px;color:#555}
</style>
</head>
<body>
<div class="top-rule"></div>
<header class="site-header">
  <div class="brand"><span class="brand-mark"></span><span class="brand-name">Veridane</span></div>
  <a class="login" href="#">Login</a>
  <nav class="main-nav">
    <a class="is-current" href="#">Features</a>
    <a class="nav-examples" href="#">Examples</a>
    <a class="nav-faq" href="#">Faq</a>
    <a class="nav-about" href="#">About</a>
  </nav>
</header>

<section class="hero" role="img" aria-label="Misty grey landscape with two figures walking across a field">
  <h1 class="hero-title">Smarter Financial Strategies</h1>
  <p class="hero-lead">Values and Cash-flow focused financial software for financial planners.</p>
  <a class="btn btn-gold" href="#">For Planning Practices</a>
  <a class="btn btn-outline" href="#">For Dealer Groups</a>
  <div class="video-frame">
    <div class="video-still" role="img" aria-label="Video player showing a smiling businessman in a meeting"></div>
  </div>
</section>

<section class="features-intro">
  <h2>The standard chunk of Lorem Ipsum</h2>
  <p>Lorem Ipsum is simply dummy text of the printing and typesetting industry. Lorem Ipsum has been the industry's standard dummy text ever since the 1500s.</p>
  <p>when an unknown printer took a galley of type and scrambled it to make a type specimen book. It has survived not only five centuries.</p>
</section>

<article class="feature-card" style="left:364px;top:678px">
  <h3>Fact Find</h3>
  <p>Contrary to popular belief, Lorem Ipsum is not text</p>
  <a class="more" href="#">Read more <svg width="14" height="6"><path d="M0 3h11M9 0l4 3-4 3z" stroke="#555" fill="#555"/></svg></a>
  <svg class="icon" viewBox="0 0 46 46"><rect x="6" y="2" width="34" height="42" rx="3" fill="none" stroke="var(--icon)" stroke-width="4"/><rect x="13" y="10" width="9" height="8" fill="var(--icon)"/><path d="M25 11h9M25 16h9M13 23h21M13 29h21M13 35h21" stroke="var(--icon)" stroke-width="3"/></svg>
</article>
<article class="feature-card is-featured" style="left:582px;top:678px">
  <h3>Online Data</h3>
  <p>Contrary to popular belief, Lorem Ipsum is not text</p>
  <a class="more" href="#">Read more <svg width="14" height="6"><path d="M0 3h11M9 0l4 3-4 3z" stroke="#6a4e18" fill="#6a4e18"/></svg></a>
  <svg class="icon" viewBox="0 0 46 46"><rect x="1" y="4" width="44" height="32" rx="3" fill="#111"/><rect x="5" y="8" width="36" height="24" fill="#d4ab4c"/><path d="M15 42h16" stroke="#111" stroke-width="4"/></svg>
</article>
<article class="feature-card" style="left:800px;top:678px">
  <h3>Custom Branding</h3>
  <p>Contrary to popular belief, Lorem Ipsum is not text</p>
  <a class="more" href="#">Read more <svg width="14" height="6"><path d="M0 3h11M9 0l4 3-4 3z" stroke="#555" fill="#555"/></svg></a>
  <svg class="icon" viewBox="0 0 46 46"><circle cx="23" cy="23" r="19" fill="none" stroke="var(--icon)" stroke-width="4"/><circle cx="23" cy="23" r="9" fill="none" stroke="var(--icon)" stroke-width="4"/><path d="M10 10l7 7M36 10l-7 7M10 36l7-7M36 36l-7-7" stroke="var(--icon)" stroke-width="6"/></svg>
</article>
<article class="feature-card" style="left:364px;top:815px">
  <h3>Site Integration</h3>
  <p>Contrary to popular belief, Lorem Ipsum is not text</p>
  <a class="more" href="#">Read more <svg width="14" height="6"><path d="M0 3h11M9 0l4 3-4 3z" stroke="#555" fill="#555"/></svg></a>
  <svg class="icon" viewBox="0 0 46 46"><path d="M12 2h22M12 44h22M14 2c0 14 16 14 16 21S14 30 14 44M32 2c0 14-16 14-16 21s16 7 16 21" fill="none" stroke="var(--icon)" stroke-width="3"/><path d="M17 40l6-8 6 8z" fill="var(--icon)"/></svg>
</article>
<article class="feature-card" style="left:582px;top:815px">
  <h3>Upload Files</h3>
  <p>Contrary to popular belief, Lorem Ipsum is not text</p>
  <a class="more" href="#">Read more <svg width="14" height="6"><path d="M0 3h11M9 0l4 3-4 3z" stroke="#555" fill="#555"/></svg></a>
  <svg class="icon" viewBox="0 0 46 46"><path d="M23 2l11 11h-6v14h-10v-14h-6z" fill="var(--icon)"/><path d="M2 30h8v8h26v-8h8v14h-42z" fill="var(--icon)"/></svg>
</article>
<article class="feature-card" style="left:800px;top:815px">
  <h3>User Management</h3>
  <p>Contrary to popular belief, Lorem Ipsum is not text</p>
  <a class="more" href="#">Read more <svg width="14" height="6"><path d="M0 3h11M9 0l4 3-4 3z" stroke="#555" fill="#555"/></svg></a>
  <svg class="icon" viewBox="0 0 46 46"><circle cx="15" cy="13" r="8" fill="var(--icon)"/><path d="M1 42c0-12 6-18 14-18s14 6 14 18z" fill="var(--icon)"/><circle cx="33" cy="16" r="7" fill="var(--icon)"/><path d="M31 42c0-8-1-12-4-15 2-1 4-2 6-2 7 0 12 5 12 17z" fill="var(--icon)"/></svg>
</article>

<div class="divider"></div>
<p class="cta-text">Create an account today and begin your 30 day trial!</p>
<a class="cta-btn" href="#">Sign Up Now !</a>

<footer class="site-footer">
  <div class="footer-rule"></div>
  <div class="footer-brand"><span class="brand-mark"></span><span class="brand-name">Veridane</span></div>
  <div class="footer-col" style="left:365px">
    <h4>About</h4>
    <ul><li>About Us</li><li>Support</li></ul>
  </div>
  <div class="footer-col" style="left:509px">
    <h4>Getting Started</h4>
    <ul><li>Why Veridane</li><li>Download a Summary</li><li>Veridane Videos</li></ul>
  </div>
  <div class="footer-col" style="left:655px">
    <h4>Legal</h4>
    <ul><li>Terms of Use</li><li>Privacy</li></ul>
  </div>
  <div class="footer-col" style="left:801px">
    <h4>Connect</h4>
    <ul><li><span class="dot dot-grey"></span>Veridane on Linkora</li><li><span class="dot dot-blue"></span>Veridane on Chirpnet</li></ul>
  </div>
  <p class="copyright">Copyright © 2014 Veridane Pty Ltd. All rights reserved.</p>
</footer>
</body>
</html>
```